Record label needs WordPress Redesign

We need a custom WordPress Redesign for our record label for women https://quillamune.com. I do not like any of the templates. We want to see something unique and modern-looking. Do NOT change the order of the sections of my homepage. Include all sections and text. My color palette is attached. The first color is my primary color #4e0f44. Only use colors from my attached palette, the only exception is white. My logo is attached. All new images that include people, people should be solely women of color. If it's a recording studio picture that includes men, it must be more women than men, and women of color must look like they are in charge.

Target Market(s)

My target market is Generation Z consumers ages 18-34

Industry/Entity Type

Music

Requirements
Must have
• My project must have all homepage sections in the same order as the original, borders, shape dividers and multi-color title text. Header-Footer primary color #4e0f44.
Nice to have
• It would be nice to see all of the colors on the palette used.
Should not have
• The homepage should not have anything from the other pages on it. The color black.

```html
<!DOCTYPE html>
<html lang="en">
<head>
<meta charset="utf-8">
<title>Quillamune — Women In Music</title>
<link rel="stylesheet" href="https://fonts.googleapis.com/css2?family=Poppins:wght@400;500;600;700;800&display=swap">
<style>
:root{
  --plum:#4e0f44;
  --magenta:#9c1c86;
  --orchid:#c257b5;
  --yellow:#fde84a;
  --navy:#142349;
  --blush:#f3cfdd;
  --mist:#f2f0f3;
  --white:#ffffff;
  --ink:#3a3552;
}
*{box-sizing:border-box;margin:0;padding:0}
html,body{width:1200px;height:5044px;overflow:hidden}
body{font-family:"Poppins",sans-serif;color:var(--navy);background:var(--white);position:relative}
section,header,footer{position:absolute;left:0;width:1200px;overflow:hidden}
.abs{position:absolute}
.photo{position:absolute}

/* HERO */
.hero{top:0;height:900px;background:linear-gradient(120deg,var(--plum) 0%,#6a1460 55%,var(--magenta) 100%)}
.hero-photo{left:0;top:0;width:560px;height:900px;background:radial-gradient(ellipse at 45% 45%,#b0468f 0%,#7a1a68 45%,rgba(78,15,68,0) 80%)}
.brand{display:flex;align-items:center;gap:12px;color:var(--white);font-weight:700;font-size:30px}
.brand-dot{width:44px;height:44px;border:3px solid var(--white);border-radius:50%}
.hero .brand{left:60px;top:40px}
.top-actions{right:80px;top:24px;display:flex;gap:18px;align-items:center}
.btn-login{border:2px solid var(--white);color:var(--white);border-radius:30px;padding:8px 26px;font-size:14px;font-weight:500}
.cart{width:40px;height:40px}
.btn-contact{background:var(--yellow);color:var(--plum);border-radius:30px;padding:10px 24px;font-size:14px;font-weight:700}
.main-nav{right:80px;top:80px;display:flex;gap:30px;color:var(--white);font-size:14px;font-weight:500;letter-spacing:.5px}
.hero-copy{left:560px;width:600px;top:340px;text-align:center}
.hero-title{font-size:58px;line-height:72px;font-weight:700;color:var(--white)}
.hero-title .accent{color:var(--yellow)}
.hero-sub{margin-top:22px;font-size:22px;font-weight:600;color:var(--white)}
.hero-btns{margin-top:36px;display:flex;flex-direction:column;align-items:center;gap:18px}
.btn-primary{background:var(--yellow);color:var(--plum);border-radius:40px;width:330px;padding:16px 0;font-size:18px;font-weight:700}
.btn-outline{border:2px solid var(--yellow);color:var(--white);border-radius:40px;width:330px;padding:14px 0;font-size:18px;font-weight:600}

/* SECTION TITLES */
.sec-title{font-size:46px;font-weight:700;letter-spacing:1px;text-align:center}
.rule{height:3px;width:90px;background:var(--magenta)}

/* RELEASES */
.releases{top:900px;height:972px;background:var(--mist)}
.releases .sec-title{position:absolute;top:128px;width:100%}
.releases .lead{position:absolute;top:210px;width:100%;text-align:center;font-size:22px;color:var(--ink)}
.releases .rule{position:absolute;top:270px;left:555px}
.release{position:absolute;top:320px;width:300px;height:420px}
.release .frame{position:absolute;left:18px;top:18px;width:300px;height:420px;border:3px solid var(--magenta)}
.release .photo{left:0;top:0;width:300px;height:420px}
.rel-1{left:72px}.rel-1 .photo{background:linear-gradient(160deg,#3d5a4c,#24352e 60%,#6b4a3a)}
.rel-2{left:440px}.rel-2 .photo{background:linear-gradient(160deg,#1f4e63,#0f2a3a 60%,#2a6a80)}
.rel-3{left:800px}.rel-3 .photo{background:linear-gradient(160deg,#c9c9cc,#6e6e74 55%,#e6e6e8)}

/* ABOUT */
.about{top:1872px;height:528px;background:var(--navy)}
.about-copy{left:72px;top:190px;width:380px;color:var(--white)}
.about-copy h2{font-size:46px;font-weight:700;text-align:left}
.about-copy .rule{margin:14px 0 24px;background:var(--yellow)}
.about-copy p{font-size:14px;line-height:24px}
.signature{margin-top:22px;width:120px;height:40px;background:linear-gradient(90deg,rgba(255,255,255,.35),rgba(255,255,255,.1))}
.about-copy .caption{margin-top:8px;font-size:11px;letter-spacing:.5px}
.about-art{left:600px;top:0;width:600px;height:528px}

/* WHAT WE DO */
.whatwedo{top:2400px;height:800px;background:var(--white)}
.whatwedo .sec-title{position:absolute;top:210px;width:100%}
.dot-big{border-radius:50%}
.service{position:absolute;top:280px;width:400px;height:380px;border-radius:22px;overflow:hidden;background:linear-gradient(180deg,var(--orchid),var(--magenta))}
.service .photo{left:0;top:0;width:400px;height:220px}
.service h3{position:absolute;left:0;width:100%;top:236px;text-align:center;color:var(--white);font-size:32px;font-weight:600}
.service p{position:absolute;left:40px;width:320px;top:292px;text-align:center;color:var(--white);font-size:13px;line-height:20px}
.svc-1{left:192px}.svc-1 .photo{background:linear-gradient(135deg,#5a2a4e,#2b1e3a 60%,#8a3a5a)}
.svc-2{left:620px}.svc-2 .photo{background:linear-gradient(135deg,#6b4a3e,#2e2230 60%,#9c6a4e)}

/* WHY WE DO IT */
.why{top:3200px;height:540px;background:var(--plum)}
.why-copy{left:72px;top:170px;color:var(--white)}
.why-copy h2{font-size:46px;font-weight:700}
.why-copy .rule{margin:12px 0 30px;background:var(--yellow)}
.why-copy .claim{font-size:40px;font-weight:700;line-height:52px;color:var(--yellow)}
.why-copy .claim .mid{color:var(--orchid)}
.study{left:640px;width:500px;top:170px;text-align:center;color:var(--white);font-size:20px;line-height:30px}
.stats{left:660px;top:270px;display:flex;gap:56px}
.stat{width:120px;text-align:center}
.stat-icon{width:100px;height:100px;margin:0 auto;border-radius:50%;background:var(--magenta);border:4px solid var(--orchid);display:flex;align-items:center;justify-content:center}
.stat h4{margin-top:12px;font-size:26px;color:var(--yellow);font-weight:700}
.stat span{font-size:22px;color:var(--white)}

/* CARE */
.care{top:3740px;height:580px;background:linear-gradient(90deg,#e9d6e6 0%,var(--blush) 60%,#f6bfd3 100%)}
.care-photo{right:0;top:0;width:560px;height:580px;background:radial-gradient(ellipse at 60% 45%,#e7b9a1 0%,#f2c6d6 50%,rgba(243,207,221,0) 80%)}
.care-copy{left:72px;top:180px;width:640px}
.care-copy h2{font-size:46px;font-weight:700;color:var(--navy)}
.care-copy .rule{margin:12px 0 34px}
.care-copy p{font-size:34px;line-height:46px;font-weight:700;color:var(--magenta)}

/* CLIENTS */
.clients{top:4320px;height:340px;background:var(--white)}
.clients h2{position:absolute;top:100px;width:100%;text-align:center;font-size:34px;font-weight:700;color:var(--navy)}
.client-row{left:200px;top:226px;width:800px;display:flex;justify-content:space-between;align-items:center;font-size:22px;font-weight:700;color:var(--navy)}
.arrow-btn{top:220px;width:44px;height:44px;border-radius:50%;background:var(--mist)}
.arrow-left{left:110px}.arrow-right{right:110px}

/* FOOTER */
.site-footer{top:4660px;height:384px;background:var(--magenta);color:var(--white)}
.site-footer .brand{left:60px;top:60px;font-size:36px}
.socials{left:60px;top:170px;display:flex;gap:10px}
.socials span{width:26px;height:26px;border:2px solid var(--white);border-radius:4px}
.f-col{top:50px}
.f-col h5{font-size:16px;font-weight:700;color:var(--yellow);letter-spacing:.5px;margin-bottom:14px}
.f-col li{list-style:none;font-size:13px;line-height:28px;display:flex;align-items:center;gap:10px}
.f-col li::before{content:"";width:8px;height:8px;background:var(--yellow);border-radius:50%}
.col-quick{left:400px}.col-extra{left:620px}.col-news{left:890px;width:260px}
.col-news p{font-size:13px;line-height:22px}
.subscribe{margin-top:16px;display:flex;align-items:center;background:var(--white);border-radius:30px;height:44px;padding:0 6px 0 18px;justify-content:space-between}
.subscribe span{color:#8b7b8a;font-size:12px}
.subscribe i{width:34px;height:34px;border-radius:50%;background:var(--yellow);display:block}
.copyright{left:0;bottom:0;width:1200px;height:44px;background:var(--plum);text-align:center;line-height:44px;font-size:12px}
</style>
</head>
<body>

<header class="hero">
  <div class="photo hero-photo" role="img" aria-label="Woman of color with braids singing into a microphone under warm stage light"></div>
  <div class="abs brand"><span class="brand-dot"></span>Quillamune</div>
  <div class="abs top-actions">
    <span class="btn-login">Login</span>
    <svg class="cart" viewBox="0 0 40 40"><circle cx="20" cy="20" r="19" fill="#fde84a"/><path d="M11 13h3l3 11h10l2-8H16" fill="none" stroke="#4e0f44" stroke-width="2"/><circle cx="18" cy="28" r="1.6" fill="#4e0f44"/><circle cx="26" cy="28" r="1.6" fill="#4e0f44"/></svg>
    <span class="btn-contact">CONTACT US</span>
  </div>
  <nav class="abs main-nav"><span>BROWSE</span><span>PLAYLISTS</span><span>ARTISTS</span><span>LICENSING</span><span>SYNCS</span><span>FAVORITES</span><span>ABOUT US</span></nav>
  <div class="abs hero-copy">
    <h1 class="hero-title">Elevate Your Projects<br><span class="accent">With Women In Music</span></h1>
    <p class="hero-sub">Your "One-Stop Shop" for 100% Pre-Cleared Music</p>
    <div class="hero-btns"><span class="btn-primary">DISCOVER TRACKS</span><span class="btn-outline">I NEED IT TAILOR-MADE</span></div>
  </div>
</header>

<section class="releases">
  <h2 class="sec-title">LATEST &amp; RELEASES</h2>
  <p class="lead">Discover talented women in music who are ready to elevate your project to new heights</p>
  <div class="rule"></div>
  <div class="release rel-1"><div class="frame"></div><div class="photo" role="img" aria-label="Album cover artwork in deep green and copper tones"></div></div>
  <div class="release rel-2"><div class="frame"></div><div class="photo" role="img" aria-label="Single cover with a woman artist in teal light"></div></div>
  <div class="release rel-3"><div class="frame"></div><div class="photo" role="img" aria-label="Monochrome release cover of a woman artist"></div></div>
</section>

<section class="about">
  <div class="abs about-copy">
    <h2>ABOUT QUILLAMUNE</h2>
    <div class="rule"></div>
    <p>Quillamune Entertainment is the first Black-owned, majority women-owned and led, independent record label and music publishing company, designed to meet the underserved needs of women in music.</p>
    <div class="signature" role="img" aria-label="Handwritten signature"></div>
    <p class="caption">DARA, CEO @ QUILLAMUNE ENTERTAINMENT</p>
  </div>
  <svg class="abs about-art" viewBox="0 0 600 528">
    <rect x="330" y="0" width="270" height="528" fill="#4e0f44"/>
    <circle cx="320" cy="268" r="262" fill="#9c1c86"/>
    <circle cx="320" cy="268" r="225" fill="#c257b5"/>
    <circle cx="320" cy="268" r="200" fill="#7a3a6a" role="img" aria-label="Woman of color wearing headphones, eyes closed, enjoying music"/>
  </svg>
</section>

<section class="whatwedo">
  <svg class="abs" style="left:30px;top:460px" width="230" height="230" viewBox="0 0 230 230"><circle cx="115" cy="115" r="112" fill="#fef3a6"/><circle cx="100" cy="100" r="92" fill="#fde84a"/></svg>
  <svg class="abs" style="left:900px;top:140px" width="220" height="220" viewBox="0 0 220 220"><circle cx="110" cy="110" r="108" fill="#fef3a6"/><circle cx="120" cy="120" r="88" fill="#fde84a"/></svg>
  <h2 class="sec-title">WHAT WE DO</h2>
  <div class="service svc-1"><div class="photo" role="img" aria-label="Women producers at a studio mixing desk"></div><h3>Music Licensing</h3><p>License music on a per-track basis or through a subscription model, providing flexibility and convenience.</p></div>
  <div class="service svc-2"><div class="photo" role="img" aria-label="Woman of color singer performing in warm light"></div><h3>Custom Music</h3><p>Discover the magic of custom music tailored to your project's needs by our team of skilled women.</p></div>
</section>

<section class="why">
  <div class="abs why-copy">
    <h2>WHY WE DO IT</h2>
    <div class="rule"></div>
    <p class="claim">WOMEN ARE<br><span class="mid">UNDERREPRESENTED</span><br>IN MUSIC</p>
  </div>
  <p class="abs study">Examined 1,200 Popular Songs From 2012 TO 2023 on the Chartwave Top 100 Year-End Charts</p>
  <div class="abs stats">
    <div class="stat"><div class="stat-icon"><svg width="46" height="46" viewBox="0 0 46 46"><circle cx="23" cy="15" r="8" fill="#fff"/><path d="M8 42c0-9 7-15 15-15s15 6 15 15z" fill="#fff"/></svg></div><h4>Artists</h4><span>35%</span></div>
    <div class="stat"><div class="stat-icon"><svg width="46" height="46" viewBox="0 0 46 46"><path d="M10 36l4-12 18-18 8 8-18 18z" fill="#fff"/></svg></div><h4>Songwriters</h4><span>19.5%</span></div>
    <div class="stat"><div class="stat-icon"><svg width="46" height="46" viewBox="0 0 46 46" stroke="#fff" stroke-width="3"><path d="M12 6v34M23 6v34M34 6v34"/><rect x="8" y="12" width="8" height="6" fill="#fff"/><rect x="19" y="26" width="8" height="6" fill="#fff"/><rect x="30" y="16" width="8" height="6" fill="#fff"/></svg></div><h4>Producers</h4><span>6.5%</span></div>
  </div>
</section>

<section class="care">
  <div class="photo care-photo" role="img" aria-label="Smiling woman of color with braids wearing headphones"></div>
  <div class="abs care-copy">
    <h2>WHY SHOULD YOU CARE</h2>
    <div class="rule"></div>
    <p>ADVANCING WOMEN'S EQUALITY COULD ADD A STAGGERING 12 TRILLION TO THE GLOBAL GDP BY 2025</p>
  </div>
</section>

<section class="clients">
  <h2>CRAFTING SOUNDSCAPES FOR THE WORLD'S BEST</h2>
  <svg class="abs arrow-btn arrow-left" viewBox="0 0 44 44"><circle cx="22" cy="22" r="22" fill="#f2f0f3"/><path d="M25 15l-7 7 7 7" fill="none" stroke="#9c1c86" stroke-width="3"/></svg>
  <div class="abs client-row"><span>Strideline</span><span>Reelhaus</span><span>Pixelvault</span><span>Voltaro</span><span>Orbique</span><span>Channelstar</span></div>
  <svg class="abs arrow-btn arrow-right" viewBox="0 0 44 44"><circle cx="22" cy="22" r="22" fill="#f2f0f3"/><path d="M19 15l7 7-7 7" fill="none" stroke="#9c1c86" stroke-width="3"/></svg>
</section>

<footer class="site-footer">
  <div class="abs brand"><span class="brand-dot"></span>Quillamune</div>
  <div class="abs socials"><span></span><span></span><span></span><span></span><span></span></div>
  <div class="abs f-col col-quick"><h5>QUICK LINKS</h5><ul><li>BROWSE</li><li>PLAYLISTS</li><li>ARTISTS</li><li>LICENSING</li><li>SYNCS</li></ul></div>
  <div class="abs f-col col-extra"><h5>ADDITIONAL LINKS</h5><ul><li>FAVORITES</li><li>ABOUT US</li><li>CONTACT US</li><li>LOGIN</li></ul></div>
  <div class="abs f-col col-news"><h5>OUR NEWSLETTER</h5><p>Subscribe to our newsletter to get the latest news.</p><div class="subscribe"><span>Enter Email Address</span><i></i></div></div>
  <div class="abs copyright">Copyright © 2024 All Rights Reserved By Company name</div>
</footer>

</body>
</html>
```